Disaster Recovery firm needs design for impactful Door Hanger flyer

We need the design for a 4.25X11 inch door hanger with die-cut included for the hanger. The hangers will be hung on the door medium to high net worth clientele's residential homes. They need to reference the event Hurricane Tova and speak to the issues that people have resulting from the storm and the benefits of our service. We will provide the sales language and bullet points.

Target Market(s)

Residential homeowners

Font styles to use
Sans Serif

Colors
3277b5
ec1f27
cee9f5
cedeed

Requirements
Must have
• Photos that include visual references to hurricane damage,
bullet points to convey the benefits of the service,
call to action, & company & local office contact information
Nice to have
• Great graphic design with layers & topics
Should not have
• Pictures of money, promises of "cash" or "no risk" and certain other violations of written statutes& compliance

```html
<!DOCTYPE html>
<html lang="en">
<head>
<meta charset="utf-8">
<title>Harborline Claims Consulting – Door Hangers</title>
<link rel="stylesheet" href="https://fonts.googleapis.com/css2?family=Roboto+Condensed:wght@400;700&family=Source+Sans+3:wght@400;600;700&display=swap">
<style>
  :root{
    --page:#ececed;
    --blue:#2f7198;
    --blue-deep:#1d3d5c;
    --blue-light:#3a86b0;
    --red:#d8202a;
    --ink:#1b1b1f;
    --white:#ffffff;
    --silver-a:#f4f4f5;
    --silver-b:#c7c8ca;
  }
  *{box-sizing:border-box;margin:0;padding:0}
  html,body{width:1074px;height:1200px;overflow:hidden;background:var(--page)}
  .canvas{position:relative;width:1074px;height:1200px}
  .hanger{position:absolute;top:75px;width:421px;height:1050px;overflow:hidden}
  .hanger--front{left:81px}
  .hanger--back{left:572px}
  .hanger__bg{position:absolute;inset:0;width:421px;height:1050px}
  .layer{position:absolute}
  .cond{font-family:"Roboto Condensed",sans-serif}
  .sans{font-family:"Source Sans 3",sans-serif}

  .headline{left:27px;top:370px;color:var(--white);line-height:1}
  .headline__lead{font-size:36px;font-weight:400;letter-spacing:-.5px}
  .headline__main{font-size:47px;font-weight:700;line-height:.98;margin-top:6px;letter-spacing:-.5px}

  .brand{left:0;width:421px;top:600px;text-align:center;color:var(--ink)}
  .brand__dot{display:block;width:34px;height:34px;border-radius:50%;background:var(--red);margin:0 auto 14px}
  .brand__name{font-size:26px;font-weight:700;letter-spacing:5px}
  .brand__sub{font-size:15px;font-weight:700;letter-spacing:5px;margin-top:2px}

  .pitch{left:0;width:421px;top:765px;text-align:center;color:var(--white);line-height:1}
  .pitch__lead{font-size:35px}
  .pitch__big{font-size:64px;font-weight:700;color:var(--red);margin:6px 0 4px;letter-spacing:-1px}
  .pitch__tail{font-size:35px}

  .contact{right:29px;top:958px;text-align:right;color:var(--ink);line-height:1}
  .contact__cta{font-size:21px;font-weight:400}
  .contact__cta b{font-weight:700}
  .contact__phones{font-size:26px;font-weight:700;margin-top:8px;display:flex;align-items:center;justify-content:flex-end;gap:7px}
  .contact__phones .sep{width:1px;height:22px;background:var(--red)}
  .contact__web{font-size:12px;margin-top:10px;display:flex;gap:14px;justify-content:flex-end;align-items:center}
  .contact__web span{display:inline-flex;align-items:center;gap:4px}

  .services-title{left:36px;top:328px;color:var(--white);font-size:44px;font-weight:700;line-height:1;letter-spacing:-.5px}
  .list{list-style:none;color:var(--ink);font-size:17px;font-weight:600;line-height:1.2}
  .list li{position:relative;padding-left:12px}
  .list--dots li::before{content:"";position:absolute;left:0;top:9px;width:5px;height:5px;border-radius:50%;background:var(--red)}
  .list--arrows li{padding-left:12px}
  .list--arrows li::before{content:"»";position:absolute;left:0;top:-1px;color:var(--red);font-weight:700}
  .svc-a{left:28px;top:418px}
  .svc-a li{margin-bottom:13px}
  .svc-b{left:229px;top:418px}
  .svc-b li{margin-bottom:14px}
  .dmg-a{left:28px;top:573px}
  .dmg-b{left:217px;top:573px}
  .dmg-a li,.dmg-b li{margin-bottom:14px}
  .rule{left:29px;top:553px;width:364px;height:1px;background:var(--blue-deep)}

  .review{right:41px;top:718px;width:345px;text-align:right;color:var(--white)}
  .review__title{font-size:24px;font-weight:700;line-height:1}
  .review__bar{display:block;width:45px;height:3px;background:var(--red);margin:8px 0 10px auto}
  .review__text{font-size:12.2px;line-height:18.2px}
  .review__text b{font-weight:700}
  .review__by{font-size:12.2px;font-weight:700;margin-top:7px}
  .review__quote{left:38px;top:855px;width:60px}
</style>
</head>
<body>
<main class="canvas">

  <!-- Front -->
  <section class="hanger hanger--front">
    <svg class="hanger__bg" viewBox="0 0 421 1050" aria-hidden="true">
      <defs>
        <linearGradient id="silver" x1="0" y1="0" x2="1" y2="1">
          <stop offset="0" stop-color="#bfc0c2"/><stop offset=".5" stop-color="#f6f6f7"/><stop offset="1" stop-color="#b9babc"/>
        </linearGradient>
        <linearGradient id="blueband" x1="0" y1="0" x2="1" y2="1">
          <stop offset="0" stop-color="#2b6a91"/><stop offset=".6" stop-color="#3279a3"/><stop offset="1" stop-color="#235a7e"/>
        </linearGradient>
      </defs>
      <rect width="421" height="1050" fill="url(#silver)"/>
      <polygon points="0,327 330,327 421,420 421,440 400,440 320,525 0,525" fill="var(--blue-deep)"/>
      <polygon points="0,354 316,354 400,437 316,525 0,525" fill="url(#blueband)"/>
      <polygon points="0,910 0,837 108,735 421,735 421,933 100,933" fill="url(#blueband)"/>
      <polygon points="0,1050 100,933 421,933 421,1050" fill="url(#silver)"/>
      <polygon points="0,1000 0,945 60,945" fill="var(--blue-light)" opacity=".6"/>
    </svg>
    <svg class="layer" style="left:0;top:0" width="421" height="327" viewBox="0 0 421 327" role="img" aria-label="Photo of a house roof and walls torn apart by a hurricane, splintered timber under a blue sky">
      <defs><linearGradient id="photoA" x1="0" y1="0" x2="0" y2="1"><stop offset="0" stop-color="#8fa4bb"/><stop offset=".45" stop-color="#8a5a44"/><stop offset="1" stop-color="#6b5240"/></linearGradient></defs>
      <rect width="421" height="327" fill="url(#photoA)"/>
      <circle cx="210" cy="138" r="58" fill="var(--page)"/>
    </svg>

    <div class="layer headline cond">
      <div class="headline__lead">WE’RE YOUR</div>
      <div class="headline__main">STORM DAMAGE<br>SOLUTION</div>
    </div>

    <div class="layer brand sans">
      <span class="brand__dot"></span>
      <div class="brand__name">HARBORLINE CLAIMS</div>
      <div class="brand__sub">CONSULTING</div>
    </div>

    <div class="layer pitch cond">
      <div class="pitch__lead">We Can Help You</div>
      <div class="pitch__big">MAXIMINE</div>
      <div class="pitch__tail">Insurance Claim Payout!</div>
    </div>

    <div class="layer contact">
      <div class="contact__cta cond">CALL US NOW FOR <b>FREE INSPECTION</b></div>
      <div class="contact__phones cond">
        <svg width="18" height="18" viewBox="0 0 24 24" aria-hidden="true"><path fill="var(--red)" d="M6.6 10.8a15 15 0 0 0 6.6 6.6l2.2-2.2c.3-.3.7-.4 1-.2 1.1.4 2.3.6 3.6.6.6 0 1 .4 1 1V20c0 .6-.4 1-1 1A17 17 0 0 1 3 4c0-.6.4-1 1-1h3.5c.6 0 1 .4 1 1 0 1.3.2 2.5.6 3.6.1.3 0 .7-.2 1z"/></svg>
        <span>877-LOSS-AID</span><span class="sep"></span><span>877-555-0142</span>
      </div>
      <div class="contact__web sans">
        <span><svg width="11" height="9" viewBox="0 0 11 9" aria-hidden="true"><rect width="11" height="9" rx="1" fill="var(--red)"/><path d="M1 1.5l4.5 3.5 4.5-3.5" stroke="#fff" fill="none"/></svg>info@harborline-claims.com</span>
        <span><svg width="11" height="11" viewBox="0 0 12 12" aria-hidden="true"><g fill="none" stroke="var(--red)" stroke-width="1.2"><circle cx="6" cy="6" r="5"/><ellipse cx="6" cy="6" rx="2.2" ry="5"/><path d="M1 6h10"/></g></svg>www.harborline-claims.com</span>
      </div>
    </div>
  </section>

  <!-- Back -->
  <section class="hanger hanger--back">
    <svg class="hanger__bg" viewBox="0 0 421 1050" aria-hidden="true">
      <rect width="421" height="1050" fill="url(#silver)"/>
      <polygon points="0,313 320,313 370,350 421,300 421,380 0,400" fill="var(--blue-deep)" opacity="0"/>
      <polygon points="0,313 230,313 360,313 318,400 0,400" fill="var(--blue-deep)"/>
      <polygon points="0,326 352,326 318,400 0,400" fill="url(#blueband)"/>
      <polygon points="0,925 0,830 106,698 421,698 421,933 100,933" fill="url(#blueband)"/>
      <polygon points="0,1050 100,933 421,933 421,1050" fill="url(#silver)"/>
      <polygon points="0,1000 0,945 60,945" fill="var(--blue-light)" opacity=".6"/>
    </svg>
    <svg class="layer" style="left:0;top:0" width="421" height="313" viewBox="0 0 421 313" role="img" aria-label="Aerial photo of a mobile home park flattened by a hurricane, debris scattered over green lawns">
      <defs><linearGradient id="photoB" x1="0" y1="0" x2="1" y2="1"><stop offset="0" stop-color="#b9b8ae"/><stop offset=".5" stop-color="#7f8f63"/><stop offset="1" stop-color="#5a6052"/></linearGradient></defs>
      <rect width="421" height="313" fill="url(#photoB)"/>
      <circle cx="210" cy="138" r="58" fill="var(--page)"/>
    </svg>

    <h2 class="layer services-title cond">OUR SERVICES</h2>

    <ul class="layer list list--dots svc-a sans">
      <li>Public Adjusters</li>
      <li>Damage Assessment<br>&amp; Loss Estimation</li>
      <li>Claims Management</li>
    </ul>
    <ul class="layer list list--dots svc-b sans">
      <li>Appraisal / Umpire</li>
      <li>Mediation</li>
      <li>Litigation Support</li>
    </ul>
    <div class="layer rule"></div>
    <ul class="layer list list--arrows dmg-a sans">
      <li>Water Damage</li>
      <li>Fire Damage</li>
      <li>Storm Damage</li>
    </ul>
    <ul class="layer list list--arrows dmg-b sans">
      <li>Hail Damage</li>
      <li>Earthquake Damage</li>
      <li>Vandalism &amp; Theft</li>
    </ul>

    <svg class="layer review__quote" viewBox="0 0 60 46" aria-hidden="true"><g fill="#5c84a6"><circle cx="14" cy="32" r="13"/><path d="M2 30C2 14 12 4 24 2l2 5C16 10 12 18 12 28z"/><circle cx="44" cy="32" r="13"/><path d="M32 30C32 14 42 4 54 2l2 5C46 10 42 18 42 28z"/></g></svg>

    <div class="layer review">
      <div class="review__title cond">HEAR OUR CLIENT SAY</div>
      <span class="review__bar"></span>
      <p class="review__text sans">After our home sustained extensive storm damage, we hired Harborline Claims Consulting to assist us in the recovery process. Although we knew that they had many other clients, Evan always made us feel as though we were their only client! Always responsive, reliable, and resourceful. We can (and do) recommend them without reservation. <b>DO NOT try to deal with the insurance company without them!</b></p>
      <div class="review__by sans">- Daniel &amp; Ruth, Mobile, AL</div>
    </div>

    <div class="layer contact">
      <div class="contact__cta cond">CALL US NOW FOR <b>FREE INSPECTION</b></div>
      <div class="contact__phones cond">
        <svg width="18" height="18" viewBox="0 0 24 24" aria-hidden="true"><path fill="var(--red)" d="M6.6 10.8a15 15 0 0 0 6.6 6.6l2.2-2.2c.3-.3.7-.4 1-.2 1.1.4 2.3.6 3.6.6.6 0 1 .4 1 1V20c0 .6-.4 1-1 1A17 17 0 0 1 3 4c0-.6.4-1 1-1h3.5c.6 0 1 .4 1 1 0 1.3.2 2.5.6 3.6.1.3 0 .7-.2 1z"/></svg>
        <span>877-LOSS-AID</span><span class="sep"></span><span>877-555-0142</span>
      </div>
      <div class="contact__web sans">
        <span><svg width="11" height="9" viewBox="0 0 11 9" aria-hidden="true"><rect width="11" height="9" rx="1" fill="var(--red)"/><path d="M1 1.5l4.5 3.5 4.5-3.5" stroke="#fff" fill="none"/></svg>info@harborline-claims.com</span>
        <span><svg width="11" height="11" viewBox="0 0 12 12" aria-hidden="true"><g fill="none" stroke="var(--red)" stroke-width="1.2"><circle cx="6" cy="6" r="5"/><ellipse cx="6" cy="6" rx="2.2" ry="5"/><path d="M1 6h10"/></g></svg>www.harborline-claims.com</span>
      </div>
    </div>
  </section>

</main>
</body>
</html>
```